Boat business cards

I'm looking for business cards with the two logos I've attached. I don't have an specific idea in mind and open to anything. All the usual info will be on the card. Name, position in company, nr, email, address, ect. The company rents out these two boats for charters and fishing.

```html
<!DOCTYPE html>
<html lang="en">
<head>
<meta charset="utf-8">
<title>Harbor Drift – Business Cards</title>
<link href="https://fonts.googleapis.com/css2?family=Arimo:wght@400;700&display=swap" rel="stylesheet">
<style>
  :root {
    --page: #2b2b2d;
    --card-top: #1a1a1c;
    --card-bottom: #060607;
    --gold: #b39a72;
    --white: #f2f2f2;
    --muted: #d8d8d8;
    --sea: #8fa9d6;
    --ink: #121213;
  }
  * { margin: 0; padding: 0; box-sizing: border-box; }
  html, body {
    width: 1200px; height: 1023px; overflow: hidden;
    background: var(--page);
    font-family: "Arimo", Arial, sans-serif;
  }
  .sheet {
    width: 1200px; height: 1023px;
    display: flex; flex-direction: column; align-items: center; justify-content: center;
    gap: 44px;
  }
  .card {
    position: relative;
    width: 700px; height: 400px;
    border-radius: 28px;
    background: linear-gradient(160deg, var(--card-top) 0%, var(--card-bottom) 75%);
    overflow: hidden;
    box-shadow: 0 14px 30px rgba(0,0,0,.45);
  }
  .boat-decor {
    position: absolute;
    background: linear-gradient(100deg, rgba(255,255,255,.0), rgba(255,255,255,.07) 40%, rgba(255,255,255,.02));
    border-radius: 6px;
  }
  .boat-art {
    position: absolute;
    background: linear-gradient(180deg, var(--white) 0%, var(--white) 38%, var(--gold) 40%, var(--gold) 78%, var(--sea) 80%, var(--sea) 100%);
    border-radius: 4px;
    opacity: .92;
  }
  .brand-name {
    position: absolute;
    color: var(--white);
    font-weight: 700;
    letter-spacing: 2px;
    text-transform: uppercase;
    white-space: nowrap;
  }

  /* front */
  .card--front .boat-decor { left: 330px; top: 150px; width: 340px; height: 150px; }
  .card--front .boat-art { left: 170px; top: 100px; width: 360px; height: 110px; }
  .card--front .brand-name { left: 0; right: 0; top: 232px; text-align: center; font-size: 44px; }

  /* back */
  .card--back .boat-decor { left: 300px; top: 150px; width: 300px; height: 140px; }
  .card--back .boat-art { left: 60px; top: 86px; width: 270px; height: 82px; }
  .card--back .brand-name { left: 60px; top: 182px; font-size: 32px; }
  .gold-tab {
    position: absolute; right: 0; top: 34px;
    width: 12px; height: 46px;
    background: var(--gold);
    border-radius: 4px 0 0 4px;
  }
  .person-name {
    position: absolute; right: 40px; top: 40px;
    color: var(--gold); font-size: 30px;
  }
  .address {
    position: absolute; right: 40px; top: 176px;
    color: var(--muted); font-size: 20px; line-height: 1.3; text-align: right;
  }
  .contacts {
    position: absolute; left: 60px; bottom: 40px;
    list-style: none; display: flex; flex-direction: column; gap: 8px;
  }
  .contacts li {
    display: flex; align-items: center; gap: 12px;
    color: var(--white); font-size: 21px;
  }
  .contacts svg { width: 24px; height: 24px; flex: none; }
</style>
</head>
<body>
<main class="sheet">
  <section class="card card--front">
    <div class="boat-decor" role="img" aria-label="Faint boat illustration in the background"></div>
    <div class="boat-art" role="img" aria-label="Illustration of a charter fishing boat on the water"></div>
    <p class="brand-name">Harbor Drift</p>
  </section>

  <section class="card card--back">
    <div class="boat-decor" role="img" aria-label="Faint boat illustration in the background"></div>
    <div class="gold-tab"></div>
    <p class="person-name">Jonathan Smith</p>
    <p class="address">Your address, city<br>state, ZIP 0000</p>
    <div class="boat-art" role="img" aria-label="Illustration of a charter fishing boat on the water"></div>
    <p class="brand-name">Harbor Drift</p>
    <ul class="contacts">
      <li>
        <svg viewBox="0 0 24 24" aria-hidden="true"><rect width="24" height="24" rx="4" fill="var(--gold)"/><path d="M8 6l2.5 0 1 3-1.5 1.2a8 8 0 0 0 3.8 3.8L15 12.5l3 1V16c0 1-1 2-2 2A11 11 0 0 1 6 8c0-1 1-2 2-2z" fill="var(--ink)"/></svg>
        123-456-2100
      </li>
      <li>
        <svg viewBox="0 0 24 24" aria-hidden="true"><rect width="24" height="24" rx="4" fill="var(--gold)"/><rect x="5" y="7" width="14" height="10" fill="none" stroke="var(--ink)" stroke-width="1.6"/><path d="M5 7l7 6 7-6M5 17l5-5M19 17l-5-5" fill="none" stroke="var(--ink)" stroke-width="1.4"/></svg>
        youremail@mail.com
      </li>
      <li>
        <svg viewBox="0 0 24 24" aria-hidden="true"><rect width="24" height="24" rx="4" fill="var(--gold)"/><circle cx="12" cy="12" r="6.5" fill="none" stroke="var(--ink)" stroke-width="1.6"/><path d="M5.5 12h13M12 5.5c-3 3.5-3 9.5 0 13M12 5.5c3 3.5 3 9.5 0 13" fill="none" stroke="var(--ink)" stroke-width="1.3"/></svg>
        www.yourwebsite.com
      </li>
    </ul>
  </section>
</main>
</body>
</html>
```